依頼詳細
【作製にあたって】
添付のラフ.xlsxは、おおまかなコンテンツ配置になります。(比率などはあまり気にしないでください。)
細部のデザインをよろしくお願いいたします。多少構成が変わっても問題ありません。

白ベースで明るくシンプルなデザインをお願いします。
サブカラー、ポイントカラーはイラストの雰囲気に合った色でお願いします。

サイト作製の目的は、信用度の向上、イラスト作製への問い合わせ増加を望んでいます。
ターゲットは、中年、お年寄りになりますので、ご留意下さい。

サイト幅は900-1000pxの間でお選び下さい。

ご不明な点はお気軽にご連絡下さい。
それではたくさんのご応募お待ちしております。

サイトURL
ページ数
1ページ
希望イメージ
シンプル 複雑
単色 カラフル
暗い 明るい
日常 高級
遊び心 厳粛
未来的 伝統的
女性的 男性的
希望する色
納品ファイル
• 高解像度JPG (.jpg)
• フォトショップ形式 (.psd)
補足説明
■ 選んだ理由

・全体的にイラストと雰囲気が合っているため。
・ターゲットや使う環境を考えた提案をして頂けた。
・またコメント内容がしっかりしており実績で高評価を獲得しているため

この3点が選んだ内容になります。
ありがとうございました。

■ 提案者全員のお礼・コメント

この度は多くのご提案頂き誠にありがとうございました。

またの11月ほどに新しくサイトを作製する予定がありますので、コンペにてご提案頂けますと幸いです。

今後ともよろしくお願い致します。

```html
<!DOCTYPE html>
<html lang="ja">
<head>
<meta charset="utf-8">
<title>遥香企画</title>
<link href="https://fonts.googleapis.com/css2?family=Noto+Sans+JP:wght@400;500;700&family=Noto+Serif+JP:wght@700&display=swap" rel="stylesheet">
<style>
:root{
  --paper:#ffffff;
  --cream:#f3efe2;
  --cream-line:#e2dcc8;
  --ink:#333333;
  --ink-soft:#666666;
  --rule:#cfcfcf;
  --accent-red:#d8332a;
  --band-grey:#ecebe8;
  --footer-dark:#2c2a26;
}
*{margin:0;padding:0;box-sizing:border-box}
html,body{width:1200px;height:2320px;overflow:hidden;background:var(--paper)}
body{position:relative;font-family:"Noto Sans JP",sans-serif;color:var(--ink)}
.abs{position:absolute}

/* header */
.header-wash{left:0;top:0;width:1200px;height:160px;background:radial-gradient(ellipse 260px 70px at 300px 40px,#e3ecd0 0,transparent 100%),radial-gradient(ellipse 220px 60px at 900px 30px,#f1e5cc 0,transparent 100%)}
.brand{left:0;top:38px;width:1200px;text-align:center;font-family:"Noto Serif JP",serif;font-weight:700;font-size:64px;line-height:80px;letter-spacing:6px;color:var(--ink)}
.request-badge{left:925px;top:4px;width:135px;height:135px;border-radius:50%;background:var(--accent-red);color:#fff;font-weight:700;font-size:19px;line-height:1.35;text-align:center;padding-top:36px}

/* nav */
.global-nav{left:0;top:160px;width:1200px;height:40px;background:var(--cream);border-bottom:1px solid var(--cream-line);display:flex;justify-content:center;gap:150px;align-items:center;font-size:17px}
.global-nav span::after,.footer-nav span::after{content:" >";color:var(--accent-red)}

/* slider */
.hero{left:0;top:215px;width:1200px;height:590px;background:
  radial-gradient(ellipse 300px 120px at 260px 430px,#b78a5a 0,transparent 100%),
  radial-gradient(ellipse 300px 120px at 900px 450px,#a9794b 0,transparent 100%),
  radial-gradient(ellipse 500px 90px at 600px 300px,#7e6f5c 0,transparent 100%),
  radial-gradient(ellipse 260px 110px at 220px 110px,#c8d2b4 0,transparent 100%),
  linear-gradient(180deg,#e3e5d6 0%,#ede1c8 50%,#d9bf98 80%,#efe5d2 100%)}
.hero-arrow{top:485px;width:44px;height:44px;border-radius:50%;background:#222;display:flex;align-items:center;justify-content:center}
.hero-arrow.prev{left:40px}.hero-arrow.next{left:1116px}

/* section titles */
.section-title{left:300px;width:600px;text-align:center;font-size:32px;font-weight:500;line-height:48px;color:var(--ink)}
.title-rule{height:2px;background:var(--rule)}

/* profile */
.profile-portrait{left:60px;top:1020px;width:300px;height:300px;border-radius:50%;background:radial-gradient(circle,#e9c3a0 0,#c9875c 55%,#e8d8c2 85%,#f7f1e7 100%)}
.profile-food{left:80px;top:1340px;width:220px;height:160px;border-radius:50%;background:radial-gradient(circle,#f0cc6a 0,#dc7446 60%,#f6eee0 100%)}
.timeline-year{left:500px;font-size:15px;line-height:28px;color:var(--ink)}
.timeline-text{left:600px;width:440px;font-size:14px;line-height:28px;color:var(--ink-soft)}

/* management */
.management{left:0;top:1520px;width:1200px;height:360px;background:var(--band-grey)}
.management-art{left:930px;top:1520px;width:270px;height:360px;background:
  radial-gradient(ellipse 100px 60px at 150px 110px,#3b3129 0,transparent 100%),
  linear-gradient(180deg,#a38d6e 0%,#6b5a46 45%,#4a3e33 70%,#c6b597 100%)}
.body-copy{left:300px;width:600px;text-align:center;font-size:15px;line-height:28px;color:var(--ink-soft)}
.link-line{left:300px;width:600px;text-align:center;font-size:30px;line-height:44px;color:var(--ink)}

/* request */
.request-art{left:40px;top:1900px;width:300px;height:330px;background:
  radial-gradient(ellipse 90px 80px at 160px 170px,#b0493c 0,transparent 100%),
  radial-gradient(ellipse 150px 150px at 150px 180px,#b8c98a 0,#d9b26a 60%,#f6f0e3 100%)}
.fish-art{left:900px;top:2140px;width:190px;height:90px;background:
  radial-gradient(ellipse 55px 28px at 60px 40px,#5f86b0 0,#a9c3da 70%,transparent 100%),
  radial-gradient(ellipse 55px 28px at 135px 55px,#5479a3 0,#a9c3da 70%,transparent 100%)}
.mail-line{left:300px;width:600px;display:flex;justify-content:center;align-items:center;gap:14px;font-size:30px;line-height:44px}

/* footer */
.footer-nav{left:0;top:2240px;width:1200px;height:50px;background:var(--cream);display:flex;justify-content:center;gap:210px;align-items:center;font-size:17px}
.copyright{left:0;top:2290px;width:1200px;height:30px;background:var(--footer-dark);color:#ddd;font-size:12px;text-align:center;line-height:30px}
</style>
</head>
<body>

<header>
  <div class="header-wash abs" role="img" aria-label="淡い水彩のにじみ装飾"></div>
  <div class="brand abs">遥香企画</div>
  <div class="request-badge abs">イラストの<br>ご依頼は<br>コチラ</div>
</header>

<nav class="global-nav abs">
  <span>⌂ トップ</span><span>▦ イラスト一覧</span><span>▤ 商品一覧</span>
</nav>

<div class="hero abs" role="img" aria-label="厨房で料理人と客が並ぶ水彩イラストのスライド"></div>
<div class="hero-arrow prev abs"><svg width="18" height="18" viewBox="0 0 18 18"><path d="M12 2 5 9l7 7" stroke="#fff" stroke-width="3" fill="none"/></svg></div>
<div class="hero-arrow next abs"><svg width="18" height="18" viewBox="0 0 18 18"><path d="M6 2l7 7-7 7" stroke="#fff" stroke-width="3" fill="none"/></svg></div>

<section class="profile">
  <h2 class="section-title abs" style="top:885px">森川遥香 プロフィール</h2>
  <div class="title-rule abs" style="left:300px;top:945px;width:600px"></div>
  <div class="profile-portrait abs" role="img" aria-label="作家の似顔絵イラスト"></div>
  <div class="profile-food abs" role="img" aria-label="料理のイラスト"></div>
  <div class="timeline-year abs" style="top:990px">1979年</div>
  <p class="timeline-text abs" style="top:990px">愛知県生まれ。<br>幼い頃から絵を描くことが好きで、絵の道を志す。<br>大学卒業後、デザイン事務所に勤務しながら<br>独学でイラストを学び、個展を重ねる。<br><br>水彩を中心とした温かみのある作風で、<br>雑誌や書籍の挿絵を多数手がける。<br>日常の何気ない風景を描くことを大切にしている。</p>
  <div class="timeline-year abs" style="top:1380px">2009年</div>
  <p class="timeline-text abs" style="top:1380px">独立し、イラスト制作の活動を本格的に開始。<br>現在も各地の依頼を受けて制作を続けている。</p>
</section>

<section class="management abs"></section>
<div class="management-art abs" role="img" aria-label="帽子をかぶった男性のイラスト"></div>
<h2 class="section-title abs" style="top:1570px">マネージメントについて</h2>
<div class="title-rule abs" style="left:300px;top:1628px;width:600px"></div>
<p class="body-copy abs" style="top:1645px">作家の活動および作品の管理は、下記の事務所にて行っております。<br>お仕事のご相談はお気軽にお問い合わせください。</p>
<div class="link-line abs" style="top:1715px">http://www.hikari-works.jp/</div>
<div class="title-rule abs" style="left:300px;top:1772px;width:600px;height:1px"></div>
<p class="body-copy abs" style="top:1790px;font-size:13px">※ 掲載作品の無断転載はご遠慮ください。</p>

<section class="request">
  <div class="request-art abs" role="img" aria-label="屋台の車と人々の水彩イラスト"></div>
  <h2 class="section-title abs" style="top:1940px">イラストのご依頼</h2>
  <div class="title-rule abs" style="left:300px;top:1998px;width:600px"></div>
  <p class="body-copy abs" style="top:2020px">イラストのご依頼・お問い合わせは下記までご連絡ください。</p>
  <div class="mail-line abs" style="top:2070px">
    <svg width="34" height="24" viewBox="0 0 34 24"><rect x="1" y="1" width="32" height="22" fill="none" stroke="#333" stroke-width="2"/><path d="M1 1l16 12L33 1" fill="none" stroke="#333" stroke-width="2"/></svg>
    <span>メール@アドレス.jp</span>
  </div>
  <div class="title-rule abs" style="left:300px;top:2128px;width:600px;height:1px"></div>
  <div class="fish-art abs" role="img" aria-label="二匹の魚のイラスト"></div>
</section>

<nav class="footer-nav abs"><span>トップ</span><span>イラスト一覧</span><span>商品一覧</span></nav>
<footer class="copyright abs">Copyright (C) 2015 遥香企画</footer>

</body>
</html>
```